Logo for Internal Medicine practice

I want a logo for my Internal Medicine practice, I would like it to be with my name on it which is Lorena Benítez Prado.

I would like the business card to say the following (it is in Spanish since my practice is in Spanish):

Lorena Benítez Prado
Medicina Interna
Cel. 5587316420
lorenabenitezprado@correovela.com

Logo Text

Lorena Benítez

```html
<!DOCTYPE html>
<html lang="es">
<head>
<meta charset="utf-8">
<title>Lorena Benítez Prado — Tarjeta de presentación</title>
<link rel="stylesheet" href="https://fonts.googleapis.com/css2?family=Montserrat:wght@500;700&display=swap">
<style>
  :root {
    --stage: #d9d9d7;
    --card-light: #fbfbfb;
    --card-dark: #1e1e1d;
    --ink: #1c1c1c;
    --ink-soft: #555555;
    --rule: #8a8a8a;
    --ghost-light: #e2e2e2;
    --ghost-dark: #3a3a39;
    --paper-white: #ffffff;
  }
  * { box-sizing: border-box; margin: 0; padding: 0; }
  html, body { width: 1200px; height: 675px; overflow: hidden; }
  body {
    background: var(--stage);
    font-family: "Montserrat", sans-serif;
    display: flex;
    align-items: center;
    justify-content: center;
    gap: 60px;
  }
  .card {
    position: relative;
    width: 520px;
    height: 300px;
    border-radius: 18px;
    overflow: hidden;
    box-shadow: 0 10px 28px rgba(0,0,0,0.18);
  }
  .card--front { background: var(--card-light); color: var(--ink); }
  .card--back { background: var(--card-dark); color: var(--paper-white); }

  .ghost-ring {
    position: absolute;
    border-radius: 50%;
    border: 2px solid var(--ghost-light);
  }
  .card--front .ghost-ring { width: 170px; height: 170px; left: -40px; top: 10px; }
  .card--back .ghost-ring { width: 190px; height: 190px; left: 30px; top: -50px; border-color: var(--ghost-dark); }

  .brand {
    position: absolute;
    display: flex;
    flex-direction: column;
    align-items: center;
    gap: 8px;
  }
  .brand__mark {
    width: 52px; height: 52px;
    border-radius: 50%;
    border: 2px solid currentColor;
  }
  .brand__name {
    font-weight: 700;
    font-size: 17px;
    letter-spacing: 0.5px;
    text-transform: uppercase;
  }
  .card--front .brand { left: 50%; top: 28px; transform: translateX(-36%); }
  .card--back .brand { left: 50%; top: 50%; transform: translate(-50%, -50%); }
  .card--back .brand__mark { width: 66px; height: 66px; }
  .card--back .brand__name { font-size: 20px; }

  .details {
    position: absolute;
    left: 34px; right: 70px;
    top: 168px;
  }
  .details__rule { height: 1px; background: var(--rule); }
  .details__rule--top { width: 220px; }
  .details__row {
    display: flex;
    justify-content: space-between;
    padding: 6px 0 10px;
  }
  .phone {
    display: flex; align-items: center; gap: 8px;
    font-weight: 700; font-size: 13px;
    margin-top: 18px;
  }
  .phone svg { width: 12px; height: 12px; }
  .identity { text-align: center; padding-left: 30px; }
  .identity__name { font-weight: 700; font-size: 13px; text-transform: uppercase; }
  .identity__role { font-weight: 500; font-size: 13px; color: var(--ink-soft); }
  .identity__email { font-weight: 500; font-size: 12px; margin-top: 12px; }
</style>
</head>
<body>
  <section class="card card--front" aria-label="Tarjeta, anverso">
    <span class="ghost-ring" aria-hidden="true"></span>
    <div class="brand">
      <span class="brand__mark" aria-hidden="true"></span>
      <span class="brand__name">Lorena Benítez</span>
    </div>
    <div class="details">
      <div class="details__rule details__rule--top"></div>
      <div class="details__row">
        <div class="phone">
          <svg viewBox="0 0 12 12" aria-hidden="true"><circle cx="6" cy="6" r="5.2" fill="none" stroke="#1c1c1c" stroke-width="1.2"/><path d="M4 3.4c.3 1.9 1.5 3.6 4 4.6l.6-.9-1-.6-.5.5c-.9-.4-1.5-1.1-1.9-2l.5-.5-.6-1z" fill="#1c1c1c"/></svg>
          <span>5587316420</span>
        </div>
        <div class="identity">
          <p class="identity__name">Lorena Benítez Prado</p>
          <p class="identity__role">Medicina Interna</p>
          <p class="identity__email">lorenabenitezprado@correovela.com</p>
        </div>
      </div>
      <div class="details__rule"></div>
    </div>
  </section>

  <section class="card card--back" aria-label="Tarjeta, reverso">
    <span class="ghost-ring" aria-hidden="true"></span>
    <div class="brand">
      <span class="brand__mark" aria-hidden="true"></span>
      <span class="brand__name">Lorena Benítez</span>
    </div>
  </section>
</body>
</html>
```